LineUp Banner for EDM music Festival!

Hello,

i need a lineup banner for an edm festival.

It should looks similar to the lineup banner uploaded here. I also added the background image.

Feel free to add something you think it looks cool.
Background have to be used. I would need after your work is done the psd file, so I can edit the text / names by myself.

Size should be around 2000x3000.

Thank you

Industry/Entity Type

Festival

Requirements
Must have
• Similar to the lineup banner. Feel free to add something you think it looks cool.
• Background have to be used.
Nice to have
• In best case it will be as most similar as the uploaded lineup banner.

```html
<!DOCTYPE html>
<html lang="en">
<head>
<meta charset="utf-8">
<title>AAA Festival – Lineup Banner</title>
<link rel="stylesheet" href="https://fonts.googleapis.com/css2?family=Anton&family=Oswald:wght@600;700&family=Roboto:wght@700&family=Roboto+Condensed:wght@400;500&display=swap">
<style>
  :root {
    --bg: #000000;
    --white: #ffffff;
    --gold: #ffd21a;
    --amber: #ff9a1a;
    --orange: #ff5a14;
    --ink: #1a0800;
    --crowd-hi: #e0a21c;
    --crowd-lo: #3a1c00;
    --glow-green: #b8d22a;
  }
  * { margin: 0; padding: 0; box-sizing: border-box; }
  html, body { width: 800px; height: 1200px; overflow: hidden; background: var(--bg); }
  .banner {
    position: relative;
    width: 800px;
    height: 1200px;
    overflow: hidden;
    background: var(--bg);
    font-family: "Roboto", Arial, sans-serif;
    color: var(--white);
  }
  .lights-art {
    position: absolute; left: 0; top: 0; width: 800px; height: 450px;
    background:
      radial-gradient(ellipse 260px 190px at 400px 190px, rgba(150,90,40,0.85), rgba(0,0,0,0) 70%),
      radial-gradient(ellipse 180px 160px at 120px 40px, rgba(40,170,60,0.8), rgba(0,0,0,0) 70%),
      radial-gradient(ellipse 200px 170px at 700px 60px, rgba(230,60,30,0.85), rgba(0,0,0,0) 70%),
      radial-gradient(ellipse 300px 140px at 400px 30px, rgba(240,200,40,0.7), rgba(0,0,0,0) 70%),
      linear-gradient(180deg, #2a1a08 0%, #120a02 70%, var(--bg) 100%);
  }
  .crowd-photo {
    position: absolute; left: 0; top: 580px; width: 800px; height: 560px;
    background:
      radial-gradient(ellipse 520px 180px at 400px 40px, rgba(184,210,42,0.75), rgba(0,0,0,0) 75%),
      linear-gradient(180deg, rgba(0,0,0,0) 0%, var(--crowd-hi) 25%, #8a5008 55%, var(--crowd-lo) 80%, var(--bg) 100%);
  }
  .presenter {
    position: absolute; top: 32px; left: 0; width: 800px; text-align: center;
    font-family: "Oswald", Impact, sans-serif; font-weight: 700;
    font-size: 40px; letter-spacing: 1px; line-height: 1;
  }
  .festival-title {
    position: absolute; top: 96px; left: 0; width: 800px; text-align: center;
    font-family: "Anton", Impact, sans-serif; font-weight: 400;
    font-size: 142px; line-height: 1; letter-spacing: 2px; white-space: nowrap;
    transform: scaleX(0.84); transform-origin: 50% 0;
    background: linear-gradient(90deg, var(--white) 0%, #fff3a0 30%, var(--gold) 55%, var(--orange) 100%);
    -webkit-background-clip: text; background-clip: text; color: transparent;
    -webkit-text-stroke: 2px var(--ink);
  }
  .event-date {
    position: absolute; top: 272px; left: 0; width: 800px; text-align: center;
    font-family: "Anton", Impact, sans-serif;
    font-size: 82px; line-height: 1; letter-spacing: 1px; white-space: nowrap;
    transform: scaleX(0.86); transform-origin: 50% 0;
    background: linear-gradient(180deg, #fff27a 0%, var(--gold) 45%, var(--amber) 70%, var(--orange) 100%);
    -webkit-background-clip: text; background-clip: text; color: transparent;
    -webkit-text-stroke: 2px var(--ink);
  }
  .lineup {
    position: absolute; top: 470px; left: 47px;
    display: grid; grid-template-columns: 375px 360px;
    list-style: none;
    font-size: 41px; line-height: 57px; font-weight: 700; white-space: nowrap;
  }
  .info-heading {
    position: absolute; top: 972px; left: 0; width: 800px; text-align: center;
    font-family: "Roboto Condensed", Arial, sans-serif; font-weight: 500; font-size: 22px;
  }
  .info-grid {
    position: absolute; top: 1015px; left: 40px;
    display: grid; grid-template-columns: 252px 261px 220px; row-gap: 8px;
    font-family: "Roboto Condensed", Arial, sans-serif; font-size: 19.5px; line-height: 22px;
    white-space: nowrap;
  }
  .sponsors-rule {
    position: absolute; top: 1124px; left: 0; width: 800px; height: 24px;
    display: flex; align-items: center; gap: 14px;
  }
  .sponsors-rule .line { flex: 1; height: 2px; background: var(--white); }
  .sponsors-rule .label {
    font-family: "Roboto Condensed", Arial, sans-serif; font-weight: 500; font-size: 21px;
  }
  .sponsor-slots {
    position: absolute; top: 1155px; left: 225px; display: flex; gap: 6px;
  }
  .sponsor-slots .slot { width: 35px; height: 35px; background: var(--white); }
</style>
</head>
<body>
<main class="banner">
  <div class="lights-art" role="img" aria-label="Disco ball with colourful party lights and sparkles"></div>
  <div class="crowd-photo" role="img" aria-label="Silhouetted festival crowd with raised hands in golden stage light"></div>

  <p class="presenter">AAA PRESENT</p>
  <h1 class="festival-title">AAA FESTIVAL</h1>
  <p class="event-date">OCTOBER 31, SUNDAY</p>

  <ul class="lineup">
    <li>DJ ARTIST NAME</li><li>DJ ARTIST NAME</li>
    <li>DJ ARTIST NAME</li><li>DJ ARTIST NAME</li>
  </ul>

  <p class="info-heading">GENERAL INFORMATIONS</p>
  <div class="info-grid">
    <span>GENERAL INFORMATIONS ▪</span><span>GENERAL INFORMATIONS ▪</span><span>GENERAL INFORMATIONS</span>
    <span>GENERAL INFORMATIONS ▪</span><span>GENERAL INFORMATIONS ▪</span><span>GENERAL INFORMATIONS</span>
    <span>GENERAL INFORMATIONS ▪</span><span>GENERAL INFORMATIONS ▪</span><span>GENERAL INFORMATIONS</span>
  </div>

  <div class="sponsors-rule"><span class="line"></span><span class="label">SPONSORS</span><span class="line"></span></div>
  <div class="sponsor-slots">
    <span class="slot"></span><span class="slot"></span><span class="slot"></span><span class="slot"></span>
    <span class="slot"></span><span class="slot"></span><span class="slot"></span><span class="slot"></span>
  </div>
</main>
</body>
</html>
```